Corporate speaking flyer for email

Redesign existing and very lame flyer. This is for my speaking business to be used as an introduction of content and style and my presentations. More photos can be provided. As you will see I'm an adventurer who makes part of my living from speaking about my adventures. The bio describes the general gist of that. There is more I could say but wanting to keep it pretty brief so as not to bore potential clients. Having said that I'd like to try and capture them in the first instance.

Target Market(s)

Corporate, clubs, events

Industry/Entity Type

Business

Requirements
Must have
• bio and references. Content provided. Feel free to edit.
Nice to have
• Surprise me!
Should not have
• Rude words.

```html
<!DOCTYPE html>
<html lang="en">
<head>
<meta charset="utf-8">
<title>Sam Carver – Speaker Flyer</title>
<link href="https://fonts.googleapis.com/css2?family=Ubuntu:ital,wght@0,300;0,400;0,500;1,300;1,400&family=PT+Sans:ital,wght@0,400;0,700;1,400&display=swap" rel="stylesheet">
<style>
:root{
  --blue:#4a6ea8;
  --blue-text:#3d63a6;
  --grey-box:#6e6e6e;
  --ink:#222;
  --paper:#fff;
  --bg:#ececec;
  --photo-warm:#b98a6a;
  --photo-mono:#9a9a9a;
  --photo-sea:#2f6fa8;
}
*{box-sizing:border-box;margin:0;padding:0}
html,body{width:1200px;height:1200px;overflow:hidden;background:var(--bg)}
body{position:relative;font-family:"PT Sans",sans-serif;color:var(--ink)}
.page{position:absolute;top:232px;width:525px;height:737px;background:var(--paper);overflow:hidden;box-shadow:0 2px 8px rgba(0,0,0,.18)}
.page--front{left:44px}
.page--back{left:618px}
.photo{position:absolute}
.photo--portrait{left:0;top:0;width:219px;height:253px;background:linear-gradient(135deg,#d9b79b,var(--photo-warm) 55%,#3a3a3a)}
.photo--stage{left:224px;top:0;width:301px;height:253px;background:linear-gradient(160deg,#e6e6e6,var(--photo-mono) 60%,#4a4a4a)}
.title-band{position:absolute;left:0;top:253px;width:525px;height:51px;background:var(--blue);color:#fff;font-family:"Ubuntu",sans-serif;font-weight:300;font-size:25px;line-height:51px;padding-left:45px;white-space:nowrap}
.title-band em{margin-left:16px;font-weight:300}
.bio{position:absolute;left:24px;top:327px;width:207px;font-size:7.3px;line-height:1.28;text-align:justify}
.bio p{margin-bottom:8px}
.bio .lead{font-weight:700;font-size:7.6px;text-align:left;margin-bottom:28px}
.bio .spacer{margin-top:30px}
.photo--boat{left:280px;top:315px;width:202px;height:140px;border:3px solid var(--blue);border-radius:8px;background:linear-gradient(180deg,#6fa0cf,var(--photo-sea) 40%,#c89572 75%,#eee)}
.feature-box{position:absolute;left:274px;top:467px;width:214px;height:219px;background:var(--grey-box);border:2px solid #d6d6d6;border-radius:8px;color:#fff;font-size:7.3px;line-height:1.27;padding:10px 14px;text-align:justify}
.feature-box p{margin-bottom:12px}
.front-footer{position:absolute;left:0;top:679px;width:525px;height:58px;background:var(--blue)}
.front-footer .web{position:absolute;left:28px;top:17px;color:#fff;font-style:italic;font-size:10px;display:flex;align-items:center;gap:4px;white-space:nowrap}
.phone-tab{position:absolute;left:249px;top:9px;width:276px;height:28px;background:#fff;border-radius:14px 0 0 14px;color:var(--blue-text);font-style:italic;font-size:9.5px;display:flex;align-items:center;padding-left:16px;gap:4px;white-space:nowrap;overflow:hidden}
.icon{width:8px;height:8px;fill:currentColor;flex:none}
.back-stripe{position:absolute;left:0;top:0;width:128px;height:737px;background:var(--blue)}
.back-stripe--thin{left:165px;width:20px}
.photo--handshake{left:21px;top:39px;width:176px;height:118px;background:linear-gradient(135deg,#8aa0a8,#b98a6a 55%,#eaeaea)}
.photo--cheer{left:72px;top:151px;width:130px;height:91px;background:linear-gradient(180deg,#1f5e9c,#3b82c4 55%,#ddd)}
.photo--speaker{left:34px;top:311px;width:150px;height:120px;background:linear-gradient(135deg,#2a2a2a,#8a7a6a 55%,#222)}
.photo--rowing{left:0;top:415px;width:115px;height:103px;background:linear-gradient(180deg,#e9a35a,#c9783e 45%,#5a7fa0)}
.framed{border:3px solid #fff;border-radius:9px;box-shadow:0 0 0 1px rgba(0,0,0,.08)}
.contact-head{position:absolute;left:0;top:587px;width:185px;height:26px;background:#fff;color:var(--blue-text);font-family:"Ubuntu",sans-serif;font-weight:500;font-size:16px;padding-left:17px;line-height:26px;white-space:nowrap}
.contact-panel{position:absolute;left:0;top:613px;width:185px;height:124px;background:var(--blue);color:#fff;font-family:"Ubuntu",sans-serif;font-size:11.5px;padding:10px 0 0 17px}
.contact-panel li{list-style:none;display:flex;align-items:center;gap:3px;height:18.5px;white-space:nowrap}
.reviews{position:absolute;left:228px;top:22px;width:266px}
.reviews h2{font-family:"Ubuntu",sans-serif;font-weight:400;font-size:19px;color:var(--blue-text);margin-bottom:12px}
.quote{font-size:6.9px;line-height:1.27;text-align:justify;margin-bottom:7px}
.quote cite{display:block;text-align:right;font-style:italic;color:var(--blue-text);margin-top:1px}
</style>
</head>
<body>

<section class="page page--front">
  <div class="photo photo--portrait" role="img" aria-label="Close-up portrait of the speaker gesturing mid-conversation"></div>
  <div class="photo photo--stage" role="img" aria-label="Black and white photo of the speaker presenting on stage to an audience"></div>
  <h1 class="title-band">Sam Carver - <em>“Anything is Possible”</em></h1>

  <div class="bio">
    <p class="lead">Whether it’s laugh out loud humour, inspiration or thought provoking anecdotes and perspective, Sam Carver’s deeply moving presentations has it all.</p>
    <p>“An extraordinary mental and physical effort – something very, very special” is how Sir Owen Hale described Sam Carver and the late Ned Varley’ incredible achievement in winning the inaugural Atlantic Rowing Race.</p>
    <p>Marathon rowing champion Sam Carver has been a New Zealand International rowing representative for 16 years. Sam’s numerous rowing achievements include World Champs silver, Commonwealth gold and a world record on the indoor rowing machine.</p>
    <p>Sam represented New Zealand at the Atlanta Olympics and published ‘The Open Oar’ on how he and Ned Varley captured headlines around the world winning the grueling and inaugural Atlantic Rowing Race in 41 days. He then led teams to successful defenses in the next two editions making it a 3-peat of victories for New Zealand.</p>
    <p class="spacer">Sam will inspire you to pursue your dreams whatever they may be, to take on new challenges, overcoming hardship against the odds and know that with passion anything is possible!</p>
    <p>It doesn’t hurt to be just a little bit crazy too!</p>
    <p>Sam’s life is about following the dream, decision making, commitment, team building, goal setting, planning, focus, determination, positive thinking and, of course, winning!</p>
  </div>

  <div class="photo photo--boat" role="img" aria-label="Two rowers celebrating on their ocean rowing boat at the finish"></div>

  <div class="feature-box">
    <p>He is co-organiser of the <em>‘River 100’ (www.river100.kiwi), ‘The Long Pull’ (www.thelongpull.co.nz)</em>, an annual rowing 8s clash between Midland and Northgate/Eastvale/Westbrook/Southfield Universities on the river.<br>His also recently conceived and managed a rowing expedition across the Tasman Sea.</p>
    <p>Ambitious goal-setting, teamwork and overcoming adversity in multiple Atlantic Rowing Race campaigns is the spine of Sam’s presentations, sandwiching the challenge of following his brother Kieran’s journey into Cambodia’s Khmer Rouge genocide www.brotherstory.co.nz (optional topic). Powerful inspiring messages on tenacity, hope, love and the last human freedom: the power to choose your attitude and how you respond in a given situation. The humour, the insights and the emotional turning points have audiences spellbound.</p>
  </div>

  <footer class="front-footer">
    <div class="web">
      <svg class="icon" viewBox="0 0 10 10"><path d="M1 3h8v5H1z M1 3l4 3 4-3" fill="none" stroke="currentColor" stroke-width="1.2"/></svg>
      sam@tideline.co.nz &nbsp;: 
      <svg class="icon" viewBox="0 0 10 10"><circle cx="5" cy="5" r="4" fill="none" stroke="currentColor" stroke-width="1.2"/><path d="M1 5h8M5 1v8" stroke="currentColor" stroke-width=".8"/></svg>
      www.samcarver.com
    </div>
    <div class="phone-tab">
      <svg class="icon" viewBox="0 0 10 10"><path d="M2 1l2 2-1 1.5c.6 1.2 1.3 1.9 2.5 2.5L7 6l2 2-1.5 1.5C4 9 1 6 .5 2.5z"/></svg>
      +64 (0)21 555 0142 &nbsp;: 
      <svg class="icon" viewBox="0 0 10 10"><path d="M2 1l2 2-1 1.5c.6 1.2 1.3 1.9 2.5 2.5L7 6l2 2-1.5 1.5C4 9 1 6 .5 2.5z"/></svg>
      +64 (0)7 555 0198
    </div>
  </footer>
</section>

<section class="page page--back">
  <div class="back-stripe"></div>
  <div class="back-stripe back-stripe--thin"></div>

  <div class="photo photo--handshake framed" role="img" aria-label="Speaker greeting an elderly man while being filmed"></div>
  <div class="photo photo--cheer framed" role="img" aria-label="Two rowers cheering aboard their ocean boat at sea"></div>
  <div class="photo photo--speaker framed" role="img" aria-label="Speaker in a suit talking at a microphone"></div>
  <div class="photo photo--rowing framed" role="img" aria-label="Single sculler rowing on golden water at sunrise"></div>

  <h2 class="contact-head">Contact Information</h2>
  <ul class="contact-panel">
    <li><svg class="icon" viewBox="0 0 10 10"><path d="M1 3h8v5H1z M1 3l4 3 4-3" fill="none" stroke="currentColor" stroke-width="1.2"/></svg>sam@tideline.co.nz</li>
    <li><svg class="icon" viewBox="0 0 10 10"><circle cx="5" cy="5" r="4" fill="none" stroke="currentColor" stroke-width="1.2"/><path d="M1 5h8M5 1v8" stroke="currentColor" stroke-width=".8"/></svg>www.samcarver.com</li>
    <li><svg class="icon" viewBox="0 0 10 10"><path d="M2 1l2 2-1 1.5c.6 1.2 1.3 1.9 2.5 2.5L7 6l2 2-1.5 1.5C4 9 1 6 .5 2.5z"/></svg>64 (0)21 555 0142</li>
    <li><svg class="icon" viewBox="0 0 10 10"><path d="M2 1l2 2-1 1.5c.6 1.2 1.3 1.9 2.5 2.5L7 6l2 2-1.5 1.5C4 9 1 6 .5 2.5z"/></svg>64 (0)7 555 0198</li>
  </ul>

  <div class="reviews">
    <h2>What clients are saying .....</h2>
    <p class="quote">“Sam has a remarkable story, told in a clever and compelling way. He is able to engage deeply with his audience; he made us laugh, cry and most importantly think deeply, as leaders, about our role in the world. One of the best!”<cite>Jane Morrow, HR Manager, Dairyfield</cite></p>
    <p class="quote">You are the second only speaker who made me cry and laugh and feel great all in one short time period, thank you so much for everything you do, and have done.....<cite>Amy Frost, Searescue conference attendee</cite></p>
    <p class="quote">“Kids Hope Trust was looking for an inspirational speaker who would reflect the passion, the hope and the commitment exhibited by the Trust and its members. When I set out to look for such a person Sam Carver’s name kept bubbling to the surface and I’m delighted I made the phone call. Sam your speech is probably the most inspiring talk I have ever listened to. Your story is an amazing one delivered in a passionate and yet entertaining manner.”<cite>Tom Reid, CEO Southport Airport</cite></p>
    <p class="quote">“... hearing your story was more inspirational than all the traditional “motivational” type trainers put together.”<cite>Luke Harte, Harte Realty</cite></p>
    <p class="quote">“The speaker was one of the most powerful I have listened to in years......incredible!”<cite>From client taken from conference feedback form</cite></p>
    <p class="quote">Sam was unbelievable, amazing, so well received, such a lovely guy, so humble. Had some of the audience in tears.<cite>Paul Dane, Meridian Broking Head</cite></p>
    <p class="quote">It was both an honour and a pleasure to be your host. The whole audience was captivated by your speech from start to finish. The clever way it was put together and how you incorporated our theme was fantastic. Your speech was truly inspirational and I personally have taken a lot out of it. The perspective on how I view challenges will change going forward as I am sure many others will too. I read a quote the other day that said ‘Don’t wait for sleep to dream’ and I think that sums it up nicely.<cite>Ruth Lane, Plains Regional Council</cite></p>
    <p class="quote">“One regular conference goer said I could organise another 50 conferences and not see a presentation as good as that.”<cite>Neil Ford, Fuelco</cite></p>
    <p class="quote">We have received nothing but the highest praise for your open and honest talk – many people have been deeply moved by your story and it was the highlight of the sessions.<cite>Kate Shaw, Meridian EA to Head</cite></p>
    <p class="quote">“Listening to Sam speak is a breath of fresh air! Too often we come across heroes that seem untouchable, unattainable. But Sam’s earthy humour and humble nature coupled with an unwavering drive and determination gives his story palpable appeal and something that the everyday person can truly connect with. Communicating with a passion that is infectious, Sam’s story is one of triumph and tragedy and provides any listener the inspiration to get beyond the mindset of ‘just getting by’ when enduring tough or challenging times. He imparts the wisdom and notion that self-belief is critical and more importantly ‘possible’ for every one of us to achieve on our own personal journey to success.”<cite>Mara Lewis, Faculty Management, Eastbay</cite></p>
    <p class="quote">Sam was outstanding. As requested he arrived early and set himself up with minimal assistance using our equipment. He was seated at the top table with some of our senior ranked officers and clearly struck a rapport early on, he skillfully (craftily) knitted some of this into the early part of his talk which was captivating and all were taken along on the roller coaster journey he portrays. He managed to lift the room initially before plummeting down into a deep and (not depressing) emotional low. This is done in such a way that he brings you along with him before raising your spirits once more and filling the room with laughter at the talks close.<br>Sam cleverly molded his message around his audience and expressed great respect for the military people in the room. This was appreciated.<br>I would highly recommend Sam to any audience.<cite>Capt Ian Moss, Regional Defence Force</cite></p>
  </div>
</section>

</body>
</html>
```